Business Card Design

We are looking for a double sided business card.

On one side would be our logo

On the Other Side

Martin Kolby
Sales and Marketing

Phone/Text Logo and 530-418-2763
Email Logo and info@plumvalepets.com
Website Logo and www.plumvalepets.com
Facebook Logo and plumvale pets
Instagram Logo and plumvale_pets

Target Market(s)

Pet owners

Contact Information for Business Card

In project description

Requirements
Must have
• Logo

```html
<!DOCTYPE html>
<html lang="en">
<head>
<meta charset="utf-8">
<title>Plumvale Pets – Business Card</title>
<link rel="stylesheet" href="https://fonts.googleapis.com/css2?family=Poppins:wght@300;400;500;600;700&display=swap">
<style>
  :root {
    --backdrop: #d3d8d8;
    --card: #1f2024;
    --orange: #f0891c;
    --gold: #f6b21a;
    --silver: #d9d9d9;
    --muted: #c9c9c9;
    --monogram: #34353b;
  }
  * { box-sizing: border-box; margin: 0; padding: 0; }
  html, body { width: 1200px; height: 960px; overflow: hidden; }
  body {
    background: var(--backdrop);
    font-family: "Poppins", sans-serif;
    position: relative;
  }
  .card {
    position: absolute;
    top: 106px;
    width: 427px;
    height: 748px;
    background: var(--card);
    border-radius: 22px;
    border-left: 4px solid var(--orange);
    border-bottom: 4px solid var(--gold);
    box-shadow: 0 14px 30px rgba(0,0,0,0.28);
  }
  .card--front { left: 144px; }
  .card--back { left: 632px; }

  .front-mark {
    position: absolute;
    left: 0; right: 0; top: 250px;
    text-align: center;
    font-weight: 600;
    font-size: 66px;
    line-height: 1.1;
    color: var(--monogram);
  }

  .center { position: absolute; left: 0; right: 0; text-align: center; }

  .brand-dot {
    position: absolute;
    left: 50%; top: 44px;
    width: 62px; height: 62px;
    margin-left: -31px;
    border-radius: 50%;
    background: var(--orange);
  }
  .brand-name {
    top: 124px;
    font-weight: 600;
    font-size: 36px;
    color: var(--silver);
    letter-spacing: 0.5px;
  }

  .person-name { top: 372px; font-size: 39px; line-height: 1.2; }
  .person-name .first { font-weight: 700; color: var(--orange); }
  .person-name .last { font-weight: 300; color: var(--silver); }
  .person-role { top: 420px; font-size: 19px; font-weight: 500; color: var(--silver); letter-spacing: 0.4px; }

  .icon-row { position: absolute; left: 0; width: 423px; height: 40px; overflow: visible; }
  .icon-row--contact { top: 461px; }
  .icon-row--social { top: 629px; }

  .contact-list { top: 516px; font-size: 19px; line-height: 25.5px; color: var(--muted); letter-spacing: 0.3px; }
  .social-list { top: 670px; font-size: 19px; line-height: 26px; color: var(--muted); letter-spacing: 0.3px; }
</style>
</head>
<body>

<section class="card card--front">
  <div class="front-mark">Plumvale<br>Pets</div>
</section>

<section class="card card--back">
  <div class="brand-dot"></div>
  <div class="center brand-name">Plumvale Pets</div>

  <div class="center person-name"><span class="first">Martin</span> <span class="last">Kolby</span></div>
  <div class="center person-role">Sales and Marketing</div>

  <svg class="icon-row icon-row--contact" viewBox="0 0 423 40" aria-hidden="true">
    <defs>
      <linearGradient id="rule-left" gradientUnits="userSpaceOnUse" x1="77" y1="0" x2="160" y2="0">
        <stop offset="0" stop-color="#f6b21a"/><stop offset="1" stop-color="#f0891c"/>
      </linearGradient>
      <linearGradient id="rule-right" gradientUnits="userSpaceOnUse" x1="249" y1="0" x2="341" y2="0">
        <stop offset="0" stop-color="#f0891c"/><stop offset="1" stop-color="#f6b21a"/>
      </linearGradient>
    </defs>
    <line x1="77" y1="20" x2="148" y2="20" stroke="url(#rule-left)" stroke-width="2.2"/>
    <line x1="270" y1="20" x2="341" y2="20" stroke="url(#rule-right)" stroke-width="2.2"/>
    <g stroke="#f0891c" stroke-width="2.5" fill="#1f2024">
      <rect x="159" y="9" width="22" height="22" transform="rotate(45 170 20)" rx="2"/>
      <rect x="198" y="9" width="22" height="22" transform="rotate(45 209 20)" rx="2"/>
      <rect x="237" y="9" width="22" height="22" transform="rotate(45 248 20)" rx="2"/>
    </g>
    <g fill="none" stroke="#fff" stroke-width="1.5" stroke-linecap="round" stroke-linejoin="round">
      <path d="M165 14 l3 0 l1.5 3.5 l-2 1.5 q1.5 3 4 4 l1.5 -2 l3.5 1.5 l0 3 q-8 0 -11.5 -11.5 z"/>
      <rect x="202" y="15" width="14" height="10"/>
      <path d="M202 15 l7 6 l7 -6"/>
      <circle cx="248" cy="20" r="6.5"/>
      <path d="M241.5 20 h13 M248 13.5 q-4 6.5 0 13 M248 13.5 q4 6.5 0 13"/>
    </g>
  </svg>

  <div class="center contact-list">
    530-418-2763<br>
    info@plumvalepets.com<br>
    www.plumvalepets.com
  </div>

  <svg class="icon-row icon-row--social" viewBox="0 0 423 40" aria-hidden="true">
    <line x1="77" y1="20" x2="159" y2="20" stroke="url(#rule-left)" stroke-width="2.2"/>
    <line x1="249" y1="20" x2="341" y2="20" stroke="url(#rule-right)" stroke-width="2.2"/>
    <g stroke="#f0891c" stroke-width="2.5" fill="#1f2024">
      <rect x="174" y="9" width="22" height="22" transform="rotate(45 185 20)" rx="2"/>
      <rect x="216" y="9" width="22" height="22" transform="rotate(45 227 20)" rx="2"/>
    </g>
    <circle cx="185" cy="20" r="6" fill="none" stroke="#fff" stroke-width="1.6"/>
    <rect x="221" y="14" width="12" height="12" rx="2" fill="none" stroke="#fff" stroke-width="1.6"/>
  </svg>

  <div class="center social-list">
    plumvale pets<br>
    plumvale_pets
  </div>
</section>

</body>
</html>
```